Redesign one screen in a mobile app

I have an app called Toasts and Tallies (available on iOS and Android). This app allows wedding guests to bet on things that happen during a wedding they are attending (think: will the groom cry when the bride walks down the aisle...). The event is set up by someone called the "event leader", typically this is the bride or the groom.

Once event details, bets, and $ values of the bets are entered, the event leader publishes the event and gets to the event detail homescreen, where they can manage their event. The three main things they can do are:

1.) Share the event with other guests to join in the betting.
2.) Edit the event -- add, change, or delete bets.
3.) Add a co-organizer. If you are the bride or the groom, you want someone else managing the event on your wedding day.

I'd like to redesign this page, make it simpler, and *focus attention on sharing the event.* The biggest goal of this page is getting event leaders to share the event. We want them to invite as many wedding guests as possible.

To that end, I would like to also introducing "sharing tiers" to entice more sharing and I'd like this to be something event leaders can easily see once they hit the event homescreen. Tiers are as follows:
Share with 1 guest, unlock co-organizer feature.
Share with 5 guests, unlock physical placard with custom QR code.
Share with 10 guests, we split our proceeds with the bride and groom.
Share with 20 guests, you are entered into $250 monthly raffle.

Some additional requests:
+ Please do not use current fonts. We want new fonts that are cleaner.
+ Share options should stay the same (copy, share, QR code)
+ Need to keep "help" question mark on page as well.
+ Maintain colors generally. Red button color must be kept as is because it's used throughout app. Slight variations to other colors OK.
+ Navigation at bottom must remain.
+ Feel free to add moving elements as well, like gifs.
+ Final design delivered in Figma.
Updates

Submissions need to be app designs. Not webpages.

The current actions shown on the page need to remain - share event, edit event, add a Co-Organizer. But the goal of the design is to make the page simpler, not more complicated.

Sharing tiers can be a separate screen, linked from the event home screen. This information does not need to live on the same page!

Target Market(s)

25-40 year olds

Industry/Entity Type

Mobile Apps - Betting

Font styles to use
Sans Serif
Other font styles liked:
• I like poppins, but open to other options.

Requirements
Must have
• Fun design that focuses on sharing an event. Design delievered in Figma.

```html
<!DOCTYPE html>
<html lang="en">
<head>
<meta charset="utf-8">
<title>Event Details</title>
<link rel="stylesheet" href="https://fonts.googleapis.com/css2?family=Poppins:wght@400;500;600;700&display=swap">
<style>
:root{
  --red:#e35a4c;
  --ink:#111217;
  --heading:#555659;
  --muted:#57585c;
  --faded:#cfd0d4;
  --hero:#f3f4f8;
  --soft:#f1f2f7;
  --ring:#ffffff;
  --line:#e6e8f0;
}
*{margin:0;padding:0;box-sizing:border-box}
html,body{width:1200px;height:4914px;overflow:hidden}
body{position:relative;background:#fff;font-family:"Poppins",sans-serif;color:var(--ink)}
.abs{position:absolute}
.hero{left:0;top:0;width:1200px;height:979px;background:var(--hero);overflow:hidden}
.title{left:0;width:1200px;top:100px;text-align:center;font-size:60px;font-weight:600;color:var(--heading)}
.cover{left:427px;top:263px;width:344px;height:344px;border-radius:50%;
  background:linear-gradient(180deg,#8a8f96 0%,#b58a4a 40%,#8d6a3b 65%,#5d6470 100%);border:6px solid #fff}
.event-name{left:0;width:1200px;top:662px;text-align:center;font-size:50px;font-weight:600;color:var(--heading)}
.meta{top:793px;font-size:38px;color:var(--muted)}
.btn{display:flex;align-items:center;justify-content:center;gap:22px;border-radius:70px;font-size:38px;font-weight:500;color:#fff;background:var(--red)}
.btn.outline{background:#fff;border:3px solid var(--red);color:var(--red);font-weight:600}
.label{font-size:36px;font-weight:600}
.body-text{font-size:36px;line-height:56px;color:var(--muted);white-space:nowrap}
.h2{font-size:50px;font-weight:600;color:var(--heading)}
.para{font-size:38px;line-height:55.5px;color:var(--ink)}
.divider{left:126px;width:952px;height:2px;background:var(--line)}
.url{left:128px;top:2238px;width:942px;height:139px;border-radius:44px;background:var(--soft);
  display:flex;align-items:center;justify-content:center;font-size:31px;color:#444}
.tier-name{font-size:35px;font-weight:600}
.tier-desc{font-size:31px;line-height:62px;color:#222;white-space:nowrap}
.locked .tier-name,.locked .tier-desc{color:var(--faded)}
.avatar{width:92px;height:92px;border-radius:50%;border:3px solid #fff}
.card{left:128px;top:4127px;width:942px;height:399px;border-radius:46px;background:var(--soft)}
.nav{left:0;top:4636px;width:1200px;height:278px;background:#fff;border-radius:64px 64px 0 0;box-shadow:0 -8px 30px rgba(0,0,0,.06)}
.nav-label{font-size:36px;color:#111;text-align:center;width:240px}
</style>
</head>
<body>

<div class="abs hero">
  <svg class="abs" style="left:0;top:0" width="1200" height="979" viewBox="0 0 1200 979" fill="none" stroke="var(--ring)" stroke-width="3">
    <circle cx="599" cy="435" r="282"/>
    <circle cx="599" cy="435" r="515"/>
    <circle cx="599" cy="435" r="740"/>
  </svg>
</div>

<svg class="abs" style="left:100px;top:115px" width="60" height="56" viewBox="0 0 60 56" fill="none" stroke="#333" stroke-width="5" stroke-linecap="round" stroke-linejoin="round">
  <path d="M55 28H6M28 5L5 28l23 23"/>
</svg>
<div class="abs title">Event Details</div>
<svg class="abs" style="left:1039px;top:112px" width="62" height="62" viewBox="0 0 62 62">
  <circle cx="31" cy="31" r="31" fill="#333"/>
  <text x="31" y="43" text-anchor="middle" font-family="Poppins,sans-serif" font-weight="700" font-size="34" fill="#fff">?</text>
</svg>

<div class="abs cover" role="img" aria-label="Event cover photo: a winding road through autumn hills"></div>
<div class="abs event-name">Ridge Drive</div>

<svg class="abs" style="left:242px;top:777px" width="78" height="80" viewBox="0 0 78 80" fill="none" stroke="#333" stroke-width="4">
  <rect x="3" y="10" width="72" height="66" rx="12"/>
  <path d="M20 2v16M58 2v16M3 28h72"/>
  <g fill="#333" stroke="none"><circle cx="22" cy="45" r="4"/><circle cx="39" cy="45" r="4"/><circle cx="56" cy="45" r="4"/><circle cx="22" cy="61" r="4"/><circle cx="39" cy="61" r="4"/><circle cx="56" cy="61" r="4"/></g>
</svg>
<div class="abs meta" style="left:351px">Feb 08 - 5:00 PM</div>
<svg class="abs" style="left:716px;top:784px" width="58" height="70" viewBox="0 0 58 70" fill="none" stroke="#333" stroke-width="4">
  <path d="M29 67C29 67 5 42 5 27a24 24 0 0 1 48 0c0 15-24 40-24 40z"/>
  <circle cx="29" cy="27" r="9"/>
</svg>
<div class="abs meta" style="left:805px">Missouri</div>

<div class="abs btn" style="left:156px;top:921px;width:430px;height:121px">
  <svg width="58" height="58" viewBox="0 0 58 58" fill="none" stroke="#fff" stroke-width="4"><circle cx="45" cy="11" r="8"/><circle cx="12" cy="29" r="8"/><circle cx="45" cy="47" r="8"/><path d="M19 25l19-10M19 33l19 10"/></svg>
  Share Event
</div>
<div class="abs btn outline" style="left:626px;top:921px;width:427px;height:121px">
  <svg width="54" height="54" viewBox="0 0 54 54" fill="var(--red)"><path d="M34 6l14 14-26 26H8V32z"/><path d="M6 50h8" stroke="var(--red)" stroke-width="4"/><path d="M30 14l10 10" stroke="#fff" stroke-width="4"/></svg>
  Edit Event
</div>

<div class="abs label" style="left:105px;top:1131px">Description</div>
<div class="abs body-text" style="left:105px;top:1199px">Lorem ipsum is a dummy text and placeholder content.<br>Lorem ipsum dolor sit amet indicint amur adipiscing ...</div>

<svg class="abs" style="left:116px;top:1385px" width="164" height="164" viewBox="0 0 164 164" fill="none" stroke="#111" stroke-width="4">
  <circle cx="82" cy="82" r="82" fill="var(--soft)" stroke="none"/>
  <rect x="49" y="57" width="46" height="58" rx="12" transform="rotate(-10 72 86)"/>
  <rect x="70" y="48" width="46" height="58" rx="12" fill="var(--soft)"/>
</svg>
<div class="abs label" style="left:311px;top:1442px">3 Bets</div>

<div class="abs avatar" style="left:118px;top:1622px;background:#6b5a4a" role="img" aria-label="Guest photo"></div>
<div class="abs avatar" style="left:163px;top:1622px;background:#8aa0a8" role="img" aria-label="Guest photo"></div>
<div class="abs avatar" style="left:209px;top:1622px;background:#3a3d44" role="img" aria-label="Guest photo"></div>
<div class="abs avatar" style="left:255px;top:1622px;background:#7c86c8" role="img" aria-label="Guest photo"></div>
<div class="abs avatar" style="left:301px;top:1622px;background:#9a9a9a" role="img" aria-label="Guest photo"></div>
<div class="abs label" style="left:414px;top:1641px;font-size:38px">+ 5 People invited</div>
<svg class="abs" style="left:1008px;top:1630px" width="76" height="76" viewBox="0 0 76 76" fill="none" stroke="var(--red)" stroke-width="4"><circle cx="38" cy="38" r="35"/><path d="M38 22v32M22 38h32"/></svg>

<div class="abs divider" style="top:1797px"></div>

<div class="abs h2" style="left:126px;top:1862px">Share Your Event</div>
<div class="abs para" style="left:126px;top:1956px;width:950px">Invite guests to join by sharing the event below. Each guest pays $1.99 to join, and if 10+ guest join in the fun, we share the proceeds with the bride and groom!</div>

<div class="abs url">https://links.toastsandtallies.com/8123asMazCe</div>

<div class="abs btn" style="left:126px;top:2438px;width:307px;height:121px">
  <svg width="50" height="50" viewBox="0 0 50 50" fill="none" stroke="#fff" stroke-width="4" stroke-linecap="round"><path d="M21 29a10 10 0 0 0 14 0l8-8a10 10 0 0 0-14-14l-4 4"/><path d="M29 21a10 10 0 0 0-14 0l-8 8a10 10 0 0 0 14 14l4-4"/></svg>
  Copy
</div>
<div class="abs btn" style="left:446px;top:2438px;width:306px;height:121px">
  <svg width="58" height="58" viewBox="0 0 58 58" fill="none" stroke="#fff" stroke-width="4"><circle cx="45" cy="11" r="8"/><circle cx="12" cy="29" r="8"/><circle cx="45" cy="47" r="8"/><path d="M19 25l19-10M19 33l19 10"/></svg>
  Share
</div>
<div class="abs btn" style="left:767px;top:2438px;width:305px;height:121px;gap:18px">
  <svg width="54" height="54" viewBox="0 0 54 54" fill="none" stroke="#fff" stroke-width="4"><rect x="3" y="3" width="19" height="19"/><rect x="32" y="3" width="19" height="19"/><rect x="3" y="32" width="19" height="19"/><g fill="#fff" stroke="none"><rect x="32" y="32" width="7" height="7"/><rect x="44" y="32" width="7" height="7"/><rect x="38" y="38" width="7" height="7"/><rect x="32" y="44" width="7" height="7"/><rect x="44" y="44" width="7" height="7"/></g></svg>
  QR Code
</div>

<div class="abs h2" style="left:126px;top:2637px">Sharing Tiers</div>
<div class="abs" style="left:126px;top:2740px;width:950px">
  <div class="tier"><div class="tier-name">Tier 1</div><div class="tier-desc" style="margin-bottom:8px">Share with 1 guest, unlock co-organizer feature.</div></div>
  <div class="tier"><div class="tier-name">Tier 2</div><div class="tier-desc" style="margin-bottom:8px">Share with 5 guests, unlock physical placard with custom<br>QR code.</div></div>
  <div class="tier locked"><div class="tier-name">Tier 3</div><div class="tier-desc" style="margin-bottom:8px">Share with 10 guests, we split our proceeds with the bride<br>and groom.</div></div>
  <div class="tier locked"><div class="tier-name">Tier 4</div><div class="tier-desc">Share with 20 guests, you are entered into $250 monthly<br>raffle.</div></div>
</div>

<div class="abs divider" style="top:3549px"></div>

<div class="abs h2" style="left:126px;top:3647px">Assign a Co-Organizer</div>
<div class="abs para" style="left:126px;top:3738px;width:940px">If a bride or groom created this event, you’ll want to assign a guest to be the co-organizer. This allows them to manage the event going forward, closing out all bets as they happen during the wedding weekend. Your co-organizer will get a notification to take over!</div>

<div class="abs card"></div>
<div class="abs h2" style="left:187px;top:4188px">Event Organizers</div>
<div class="abs" style="left:193px;top:4325px;width:126px;height:126px;border-radius:50%;background:#9fae9a" role="img" aria-label="Organizer profile photo"></div>
<div class="abs" style="left:357px;top:4352px;font-size:53px;color:#222">Toby Rollins</div>
<svg class="abs" style="left:927px;top:4350px" width="76" height="76" viewBox="0 0 76 76" fill="none" stroke="var(--red)" stroke-width="4"><circle cx="38" cy="38" r="35"/><path d="M38 22v32M22 38h32"/></svg>

<nav class="abs nav">
  <svg class="abs" style="left:191px;top:40px" width="164" height="164" viewBox="0 0 164 164">
    <circle cx="82" cy="82" r="82" fill="var(--red)"/>
    <path d="M58 80l24-20 24 20v26H58z" fill="none" stroke="#fff" stroke-width="5" stroke-linejoin="round"/>
    <path d="M82 86v8" stroke="#fff" stroke-width="5" stroke-linecap="round"/>
  </svg>
  <svg class="abs" style="left:555px;top:66px" width="84" height="80" viewBox="0 0 84 80" fill="none" stroke="#111" stroke-width="4">
    <rect x="8" y="18" width="40" height="54" rx="12" transform="rotate(-10 28 45)"/>
    <rect x="32" y="8" width="42" height="56" rx="12" fill="#fff"/>
  </svg>
  <div class="abs nav-label" style="left:477px;top:144px">My Bets</div>
  <svg class="abs" style="left:890px;top:62px" width="76" height="80" viewBox="0 0 76 80" fill="none" stroke="#111" stroke-width="4" stroke-linejoin="round">
    <path d="M38 4l3 6 6 1-4 4 1 6-6-3-6 3 1-6-4-4 6-1z"/>
    <path d="M28 76V30h20v46M8 76V48h20M48 50h20v26M2 76h72"/>
  </svg>
  <div class="abs nav-label" style="left:807px;top:144px">Leaders</div>
</nav>

</body>
</html>
```